Celebrating 50 Years of Brantwick

This will be a vinyl 10 foot by 8 foot large banner hung at a 50 year celebration. Attached you will find the word document that it will need to have on it and the logo and the invitation - both in all different formats - be creative as possible while staying with brand. We want a dynamic representation of the accomplishments over the last 50 years.

Target Market(s)

To use at a function to celebrate our 50th years in business

Industry/Entity Type

Hospitality

Colors

Designer to choose colors to be used in the design.

Requirements
Must have
• the attached logo and the events
Nice to have
• branding to tie into
Should not have
• should not boring and appear flat

```html
<!DOCTYPE html>
<html lang="en">
<head>
<meta charset="utf-8">
<title>Brantwick Family History – 50 Years of Hospitality</title>
<link rel="stylesheet" href="https://fonts.googleapis.com/css2?family=Libre+Baskerville:ital,wght@0,400;0,700;1,400&family=Cormorant+Garamond:ital,wght@0,300;0,400;1,400&family=EB+Garamond:wght@400;600&family=Great+Vibes&display=swap">
<style>
:root{
  --brand-blue:#1c72b8;
  --year-blue:#1f7fd0;
  --panel-blue-1:#1d9ee0;
  --panel-blue-2:#1670c4;
  --canvas-gray:#a5a6aa;
  --header-gray:#d4d5d8;
  --muted-gray:#d6d7da;
  --white:#ffffff;
}
*{margin:0;padding:0;box-sizing:border-box}
html,body{width:1200px;height:960px;overflow:hidden}
body{position:relative;background:var(--canvas-gray);font-family:"Libre Baskerville",Georgia,serif;color:var(--white);font-variant-numeric:lining-nums}

.brand-area{position:absolute;left:0;top:0;width:752px;height:332px;background:linear-gradient(180deg,#fbfbfb 0%,#e3e4e5 60%,#cfd0d2 100%)}
.brand-lockup{position:absolute;left:150px;top:110px;display:flex;align-items:center;gap:22px}
.brand-mark{width:110px;height:110px;border-radius:50%;border:8px solid var(--brand-blue)}
.brand-name{font-family:"Libre Baskerville",Georgia,serif;font-weight:700;font-size:40px;color:var(--brand-blue);line-height:1.15}

.history-title{position:absolute;left:78px;top:354px;font-size:31px;font-weight:700;color:var(--brand-blue);white-space:nowrap;line-height:1}
.history-rule{position:absolute;left:82px;top:399px}
.history-subtitle{position:absolute;left:78px;top:408px;font-family:"Cormorant Garamond",Georgia,serif;font-weight:300;font-size:46px;line-height:1.1;color:var(--white);letter-spacing:.5px;white-space:nowrap}

.invitation{position:absolute;left:752px;top:0;width:448px;height:452px;background:#e6e7e8;padding:0 0 7px 6px}
.invitation-card{position:relative;width:100%;height:100%;background:linear-gradient(160deg,var(--panel-blue-1) 0%,var(--panel-blue-2) 100%);text-align:center;font-family:"Libre Baskerville",Georgia,serif}
.invite-lead{position:absolute;left:0;right:0;top:32px;font-family:"Cormorant Garamond",Georgia,serif;font-size:18.5px;line-height:22px}
.invite-fifty{position:absolute;left:150px;top:62px;font-family:"Great Vibes",cursive;font-size:150px;line-height:1;color:transparent;-webkit-text-stroke:2px var(--white)}
.invite-years{position:absolute;left:155px;top:160px;font-family:"Great Vibes",cursive;font-size:62px;color:var(--white)}
.invite-business{position:absolute;left:200px;top:212px;font-family:"Cormorant Garamond",Georgia,serif;font-size:19px}
.invite-rule{position:absolute}
.invite-label{font-family:"Cormorant Garamond",Georgia,serif;font-style:italic;font-size:18px}
.invite-date{position:absolute;left:100px;top:244px;width:120px}
.invite-date .day{font-family:"Cormorant Garamond",Georgia,serif;font-size:19px;line-height:22px}
.invite-date .when{font-weight:700;font-size:17px}
.invite-divider{position:absolute;left:225px;top:244px;width:1.5px;height:62px;background:var(--white)}
.invite-time{position:absolute;left:232px;top:244px;width:150px}
.invite-time .hours{font-family:"Cormorant Garamond",Georgia,serif;font-size:19px;margin-top:4px}
.invite-where{position:absolute;left:0;right:0;top:314px;font-family:"Cormorant Garamond",Georgia,serif;font-size:19px;line-height:21px}
.invite-phone{position:absolute;left:0;right:0;top:385px;font-family:"Cormorant Garamond",Georgia,serif;font-size:18px;line-height:21px}
.hr{position:absolute;height:1.5px;background:var(--white)}

.timeline{position:absolute;top:488px}
.timeline-range{display:flex;align-items:center;font-family:"Cormorant Garamond",Georgia,serif;font-size:21px;color:var(--header-gray);height:24px;margin-bottom:10px}
.timeline-list{list-style:none;border-left:2px solid var(--white);padding-left:6px}
.timeline-list li{font-family:"EB Garamond",Georgia,serif;font-size:8.6px;line-height:13.9px;height:13.9px;white-space:nowrap;font-weight:600;color:var(--white)}
.timeline-list .yr{display:inline-block;width:28px;color:var(--year-blue)}
.timeline-list li.early{color:var(--muted-gray);font-weight:400}
.timeline-list li.early .yr{color:#6f7074}
.col-1{left:37px;width:320px}
.col-2{left:366px;width:400px}
.col-3{left:773px;width:420px}
</style>
</head>
<body>

<section class="brand-area">
  <div class="brand-lockup">
    <div class="brand-mark"></div>
    <div class="brand-name">Brantwick<br>Hospitality</div>
  </div>
</section>

<h1 class="history-title">BRANTWICK FAMILY HISTORY</h1>
<svg class="history-rule" width="578" height="10" viewBox="0 0 578 10">
  <line x1="6" y1="5" x2="572" y2="5" stroke="#fff" stroke-width="1.5"/>
  <polygon points="0,5 8,1 16,5 8,9" fill="#fff"/>
  <polygon points="562,5 570,1 578,5 570,9" fill="#fff"/>
</svg>
<h2 class="history-subtitle">50 YEARS OF HOSPITALITY</h2>

<aside class="invitation">
  <div class="invitation-card">
    <p class="invite-lead">Brantwick family cordially Invites you to a<br>luncheon to Celebrate</p>
    <div class="invite-fifty">50</div>
    <div class="invite-years">years</div>
    <div class="invite-business">of business!</div>
    <svg class="invite-rule" style="left:130px;top:236px" width="175" height="8" viewBox="0 0 175 8">
      <line x1="4" y1="4" x2="171" y2="4" stroke="#fff" stroke-width="1.2"/>
      <polygon points="0,4 6,1 6,7" fill="#fff"/><polygon points="175,4 169,1 169,7" fill="#fff"/>
    </svg>
    <div class="invite-date">
      <div class="invite-label">Date:</div>
      <div class="day">Tuesday</div>
      <div class="when">May 15 2018</div>
    </div>
    <div class="invite-divider"></div>
    <div class="invite-time">
      <div class="invite-label">Time:</div>
      <div class="hours">11 am - 1 pm</div>
    </div>
    <div class="hr" style="left:70px;width:288px;top:311px"></div>
    <div class="invite-where">
      <div class="invite-label">Where:</div>
      Alder Creek Center 1450 Laurel Lane<br>Cedar Forge TN 37000
    </div>
    <div class="hr" style="left:68px;width:285px;top:384px"></div>
    <div class="invite-phone">
      <div class="invite-label">Phone number:</div>
      555-014-2187
    </div>
  </div>
</aside>

<section class="timeline col-1">
  <div class="timeline-range">1968<svg width="170" height="8" viewBox="0 0 170 8"><line x1="6" y1="4" x2="164" y2="4" stroke="#d4d5d8"/><polygon points="0,4 5,1 10,4 5,7" fill="#d4d5d8"/><polygon points="80,4 85,2 90,4 85,6" fill="#d4d5d8"/><polygon points="170,4 164,1 164,7" fill="#d4d5d8"/></svg>1990</div>
  <ul class="timeline-list">
    <li class="early"><span class="yr">1963</span>Purchased Ridgeview Skies Property</li>
    <li class="early"><span class="yr">1963</span>Purchased Hickory Hank's Barbeque Property</li>
    <li class="early"><span class="yr">1965</span>Purchased Golden Harvest Buffet Property &amp; Thornwood Inn Property</li>
    <li class="early"><span class="yr">1967</span>Purchased Cedar Grove Property</li>
    <li><span class="yr">1968</span>Opened 1st Motel at Ridgeview Skies Property (22 Units)</li>
    <li><span class="yr">1971</span>Opened Blue Ridge Pancake House</li>
    <li><span class="yr">1971</span>Purchased Laurel River Court (35 Units)/Now Brookstone Inn</li>
    <li><span class="yr">1971</span>Opened 2nd Building at Ridgeview Skies Property (20 Units)</li>
    <li><span class="yr">1972</span>Opened 3rd Building at Ridgeview Skies Property (39 Units)</li>
    <li><span class="yr">1972</span>Opened Copperhead Kingdom</li>
    <li><span class="yr">1973</span>Purchased Campground (10 Acres)/Now Camp Riverbend</li>
    <li><span class="yr">1973</span>Purchased Cabanas/Now Brookstone Inn at Riverbend Landing</li>
    <li><span class="yr">1974</span>Opened and Built Canaan Motel (20 Units)</li>
    <li><span class="yr">1975</span>Built and Added 12 Units to Ridgeview Skies Property</li>
    <li><span class="yr">1976</span>Built and Added Blue Ridge Pancake House to Ridgeview Skies Property</li>
    <li><span class="yr">1976</span>Remodeled and Opened Retail Beverage Store</li>
    <li><span class="yr">1977</span>Built and Opened World's Largest Water Slide</li>
    <li><span class="yr">1978</span>Purchased Uncle Abe's Property/The Old Halverson Farm</li>
    <li><span class="yr">1979</span>Built and Opened Gas Station Pronto Mart</li>
    <li><span class="yr">1982</span>Remodeled and Opened Uncle Abe's Pancake House</li>
    <li><span class="yr">1982</span>Built and Opened Thrifty Barn</li>
    <li><span class="yr">1986</span>Construction Company Started – Brantwick Construction</li>
    <li><span class="yr">1986</span>Built and Opened Thornwood Inn (57 Units)</li>
    <li><span class="yr">1987</span>Remodeled and Added 23 Units to Ridgeview Skies Property</li>
    <li><span class="yr">1988</span>Built and Added 45 Units to Canaan Motel</li>
    <li><span class="yr">1989</span>Blue Ridge Resorts Brand Developed</li>
    <li><span class="yr">1989</span>Built and Opened Brookstone Inn (112 Units)</li>
    <li><span class="yr">1990</span>Purchased Drive-In Theater Property</li>
    <li><span class="yr">1990</span>Remodeled and Opened Blue Ridge Pancake House</li>
    <li><span class="yr">1990</span>Blue Ridge Receptive Brand Developed</li>
  </ul>
</section>

<section class="timeline col-2">
  <div class="timeline-range">1991<svg width="170" height="8" viewBox="0 0 170 8"><line x1="6" y1="4" x2="164" y2="4" stroke="#d4d5d8"/><polygon points="0,4 5,1 10,4 5,7" fill="#d4d5d8"/><polygon points="80,4 85,2 90,4 85,6" fill="#d4d5d8"/><polygon points="170,4 164,1 164,7" fill="#d4d5d8"/></svg>1999</div>
  <ul class="timeline-list">
    <li><span class="yr">1991</span>Built and Opened Valley Crest Lodge/Now Parkway Inn (62 Units)</li>
    <li><span class="yr">1991</span>Built and Opened Valley Crest Winery</li>
    <li><span class="yr">1992</span>Built and Opened 62 Unit Addition to Valley Crest Lodge/Now Parkway Inn</li>
    <li><span class="yr">1993</span>Replaced Uncle Abe's Pancake House with Homestyle Kitchen (#1 in the World)</li>
    <li><span class="yr">1994</span>Awarded Rising 50 – Riverton Metro Area</li>
    <li><span class="yr">1994</span>Opened Orchard Barn Winery</li>
    <li><span class="yr">1994</span>Built and Opened Laserzone a Family Entertainment Center</li>
    <li><span class="yr">1994</span>Built and Opened Hearthside Inn &amp; Suites (138 Units)/Now Hearthside Cascades Waterpark Resort</li>
    <li><span class="yr">1995</span>Awarded Rising 50 – Riverton Metro Area</li>
    <li><span class="yr">1995</span>Built and Opened Brookstone Inn at Riverbend Landing (60 Units)</li>
    <li><span class="yr">1995</span>Built and Opened Blue Ridge Convention Center</li>
    <li><span class="yr">1995</span>Replaced Blue Ridge Pancake House with Golden Harvest Buffet Cedar Forge (#1 in the World)</li>
    <li><span class="yr">1996</span>Awarded Rising 50 – Riverton Metro Area</li>
    <li><span class="yr">1996</span>Built and Opened Hickory Hank's BBQ and Ribs</li>
    <li><span class="yr">1996</span>Built and Opened Summit Chemical</li>
    <li><span class="yr">1996</span>Built and Opened Golden Harvest Buffet in Ashford</li>
    <li><span class="yr">1996</span>Purchased Statesman's Crossing Property</li>
    <li><span class="yr">1996</span>Opened Frosty Cone</li>
    <li><span class="yr">1997</span>Awarded Rising 50 – Riverton Metro Area</li>
    <li><span class="yr">1997</span>Purchased Bel Vista Mountain Inn/Bel Vista Lodge</li>
    <li><span class="yr">1997</span>Purchased Hearthwood Suites</li>
    <li><span class="yr">1997</span>Built and Opened Weekend Grill Ashford</li>
    <li><span class="yr">1997</span>Built and Opened Mr. Rossi's Pizza</li>
    <li><span class="yr">1997</span>Brantwick Development Company Reorganized Into Separate Divisions</li>
    <li><span class="yr">1998</span>Awarded Rising 50 – Riverton Metro Area</li>
    <li><span class="yr">1998</span>Opened Salty Pete's Lighthouse Grill/Highway 9 Roadhouse</li>
    <li><span class="yr">1999</span>Built Daybreak Donuts/Scoops Ice Cream in Ashford</li>
    <li><span class="yr">1999</span>Awarded Tourism Leader of the Year – City of Cedar Forge</li>
    <li><span class="yr">1999</span>Built and Opened Weekend Grill Hollowburg</li>
    <li><span class="yr">1999</span>Built and Opened Stony Creek Grille</li>
  </ul>
</section>

<section class="timeline col-3">
  <div class="timeline-range">1999<svg width="170" height="8" viewBox="0 0 170 8"><line x1="6" y1="4" x2="164" y2="4" stroke="#d4d5d8"/><polygon points="0,4 5,1 10,4 5,7" fill="#d4d5d8"/><polygon points="80,4 85,2 90,4 85,6" fill="#d4d5d8"/><polygon points="170,4 164,1 164,7" fill="#d4d5d8"/></svg>2018</div>
  <ul class="timeline-list">
    <li><span class="yr">1999</span>Built and Opened Statesman's Crossing Outlet Mall</li>
    <li><span class="yr">1999</span>Built and Opened Statesman's Palace</li>
    <li><span class="yr">2000</span>Opened Seven Elms Steakhouse</li>
    <li><span class="yr">2001</span>Opened Daybreak Donuts/Scoops Ice Cream in Brookside</li>
    <li><span class="yr">2001</span>Built and Opened Statesman's Inn</li>
    <li><span class="yr">2001</span>Built and Opened 1st Griddlecakes Pancake Cabin in Ashford</li>
    <li><span class="yr">2002</span>Opened 2nd Griddlecakes Pancake Cabin in Hollowburg off Hwy 321</li>
    <li><span class="yr">2004</span>Opened 3rd Griddlecakes Pancake Cabin in Hollowburg off Hwy 441</li>
    <li><span class="yr">2004</span>Built and Opened The Resort at Statesman's Crossing Phase I</li>
    <li><span class="yr">2005</span>Opened 4th Griddlecakes Pancake Cabin in Cedar Forge</li>
    <li><span class="yr">2005</span>Built and Opened The Resort at Statesman's Crossing Phase II</li>
    <li><span class="yr">2007</span>Opened 5th Griddlecakes Pancake Cabin in Millton</li>
    <li><span class="yr">2007</span>Built and Opened The Resort at Statesman's Crossing Indoor Waterpark</li>
    <li><span class="yr">2007</span>Opened Hickory Hank's BBQ in Hollowburg</li>
    <li><span class="yr">2008</span>Opened 6th Griddlecakes Pancake Cabin in Hollowburg</li>
    <li><span class="yr">2009</span>Built and Opened Hilltop Winery</li>
    <li><span class="yr">2011</span>Opened Sugarbrook Cellars</li>
    <li><span class="yr">2011</span>Opened Fondue Kettle</li>
    <li><span class="yr">2012</span>Remodeled and Opened Hawk Springs Winery in Millton</li>
    <li><span class="yr">2014</span>Opened Doc Brantwick Moonshine in Hollowburg</li>
    <li><span class="yr">2015</span>Remodeled and Opened Stonebridge Winery at the Old Forge District</li>
    <li><span class="yr">2015</span>Opened Sugarbrook Cellars Tasting Room in Hollowburg</li>
    <li><span class="yr">2015</span>Replace Mr. Rossi's Pizza with Gearhead Wings &amp; Grill</li>
    <li><span class="yr">2016</span>Built and Opened Griddlecakes Sandpiper Beach</li>
    <li><span class="yr">2017</span>Built and Opened Windy City Pizza Sandpiper Beach</li>
    <li><span class="yr">2017</span>Opened Blue Ridge Pancake House Cedar Forge</li>
    <li><span class="yr">2017</span>Built and Opened The Pinnacle Tower and Cascades Waterpark at Hearthside Cascades/Waterpark Resort</li>
    <li><span class="yr">2017</span>Built and Opened Alder Creek Center</li>
    <li><span class="yr">2017</span>Built and Opened Brantwick Restaurant Group Office</li>
    <li><span class="yr">2018</span>Building Phase III of The Resort at Statesman's Crossing</li>
  </ul>
</section>

</body>
</html>
```